Bellwether Home Inspections

We need stationery for our new home inspection company. We inspect homes for people prior to purchasing to ensure the property is in good condition, as well as inspecting new homes to ensure they have been built to the appropriate standards. We are happy to look at combinations of colours. The use of a water mark would be good. Open to suggestions.

Industry/Entity Type

Home Inspection

```html
<!DOCTYPE html>
<html lang="en">
<head>
<meta charset="utf-8">
<title>Bellwether Home Inspections – Stationery</title>
<link href="https://fonts.googleapis.com/css2?family=Questrial&family=Open+Sans:wght@400;600&family=Tinos&display=swap" rel="stylesheet">
<style>
  :root{
    --brand-blue:#0b4ea8;
    --deep-blue:#0a47a0;
    --stripe-grey:#b3bdc6;
    --flap-grey:#86a3ab;
    --paper:#ffffff;
    --paper-shade:#eef0f2;
    --watermark:#e9edf2;
    --ink:#222;
    --backdrop:#7d5234;
    --label:#ffffff;
  }
  *{box-sizing:border-box;margin:0;padding:0}
  html,body{width:1200px;height:596px;overflow:hidden}
  body{background:var(--backdrop);position:relative;font-family:"Questrial",sans-serif}
  .sheet{position:absolute;background:var(--paper);overflow:hidden}

  /* brand lockup */
  .brand{position:absolute;text-align:center;color:var(--brand-blue);font-family:"Questrial",sans-serif;line-height:1.05}
  .brand-mark{display:block;margin:0 auto 4px;background:var(--brand-blue)}
  .watermark{position:absolute;background:var(--watermark)}

  /* footers */
  .footer-rule{position:absolute;left:0;right:0;background:var(--stripe-grey)}
  .footer-band{position:absolute;left:0;right:0;bottom:0;background:var(--deep-blue);color:#fff;
    font-family:"Tinos",serif;text-align:center;font-size:6.4px;line-height:11px;padding-top:2px;letter-spacing:.2px}
  .footer-band span{margin:0 3px}

  /* letterhead */
  .letterhead{left:16px;top:78px;width:338px;height:436px}
  .letterhead .brand{left:0;right:0;top:10px;font-size:10px}
  .letterhead .brand-mark{width:22px;height:22px}
  .letterhead .watermark{left:78px;top:118px;width:186px;height:186px}
  .letterhead .footer-rule{bottom:29px;height:3px}
  .letterhead .footer-band{height:25px}

  /* fax */
  .fax{left:410px;top:81px;width:338px;height:437px}
  .fax .brand{left:14px;top:10px;font-size:10px;width:90px}
  .fax .brand-mark{width:22px;height:22px}
  .fax .address{position:absolute;left:259px;top:29px;border-left:1px solid #555;padding-left:5px;
    font-family:"Tinos",serif;font-size:6px;line-height:8px;color:var(--ink)}
  .fax .title{position:absolute;left:18px;top:92px;font-family:"Open Sans",sans-serif;font-size:21px;color:var(--ink)}
  .fax .field{position:absolute;border-bottom:1px solid #444;height:10px;font-family:"Open Sans",sans-serif;
    font-size:5.5px;color:var(--ink)}
  .fax .field.left{left:18px;width:168px}
  .fax .field.right{left:189px;width:117px}
  .fax .checks{position:absolute;left:18px;top:213px;display:flex;gap:13px;font-family:"Open Sans",sans-serif;font-size:5.6px;color:var(--ink)}
  .fax .checks label{display:flex;align-items:center;gap:6px}
  .fax .checks i{width:8px;height:8px;border:1px solid #333;display:inline-block}
  .fax .watermark{left:112px;top:290px;width:116px;height:116px}
  .fax .footer-rule{bottom:24px;height:3px}
  .fax .footer-band{height:20px;line-height:16px}

  /* envelopes */
  .envelope-back{position:absolute}
  .envelope-front{left:764px;top:242px;width:379px;height:169px;background:linear-gradient(135deg,#fff 0%,#fff 40%,var(--paper-shade) 100%)}
  .envelope-front .brand{left:8px;top:10px;font-size:10.5px;width:90px}
  .envelope-front .brand-mark{width:22px;height:22px}
  .envelope-front .watermark{left:250px;top:30px;width:110px;height:110px}
  .envelope-front .footer-rule{bottom:14px;height:3px}
  .envelope-front .footer-band{height:13px;display:flex;justify-content:space-between;padding:0 9px;line-height:10px;font-size:6.4px;text-align:left}

  /* business cards */
  .card-front{left:786px;top:439px;width:139px;height:80px;background:linear-gradient(90deg,#fff 0%,#fff 50%,var(--paper-shade) 100%)}
  .card-front .brand{left:4px;top:14px;width:70px;font-size:7px}
  .card-front .brand-mark{width:15px;height:15px;margin-bottom:3px}
  .card-front .person{position:absolute;left:74px;top:13px;font-family:"Tinos",serif;color:var(--ink)}
  .card-front .person strong{display:block;font-size:5.5px}
  .card-front .person em{display:block;font-style:normal;font-size:3.8px;margin-bottom:5px}
  .card-front .person p{font-size:3.5px;line-height:6px}
  .card-front .footer-band{height:8px;font-size:3.6px;line-height:6px;padding-top:1px}
  .card-back{left:935px;top:439px;width:139px;height:80px;background:var(--deep-blue);color:#fff;text-align:center}
  .card-back .watermark{left:48px;top:12px;width:44px;height:44px;background:rgba(255,255,255,.12)}
  .card-back h2{position:relative;font-family:"Questrial",sans-serif;font-weight:400;font-size:12.5px;line-height:13px;margin-top:20px}
  .card-back p{position:relative;font-family:"Tinos",serif;font-size:5.4px;letter-spacing:.6px;margin-top:3px}

  .option-label{position:absolute;top:533px;color:var(--label);font-family:"Open Sans",sans-serif;font-size:24px;transform:translateX(-50%)}
</style>
</head>
<body>

  <!-- Letterhead -->
  <section class="sheet letterhead">
    <div class="watermark" role="img" aria-label="Faint brand watermark"></div>
    <div class="brand"><i class="brand-mark"></i>Bellwether<br>Home Inspections</div>
    <div class="footer-rule"></div>
    <div class="footer-band">
      <span>✆ 555-014-2290</span><span>✆ 555-014-2256</span><span>✉ hello@bellwetherinspect.com</span><span>www.bellwetherinspect.com</span><br>
      Street Name, City Name State Zipcode
    </div>
  </section>

  <!-- Fax sheet -->
  <section class="sheet fax">
    <div class="brand"><i class="brand-mark"></i>Bellwether<br>Home Inspections</div>
    <div class="address">Street Name, City Name<br>State Zipcode</div>
    <h1 class="title">FAX</h1>
    <div class="field left" style="top:148px">To :</div>
    <div class="field right" style="top:148px">From :</div>
    <div class="field left" style="top:166px">Fax :</div>
    <div class="field right" style="top:166px">Pages :</div>
    <div class="field left" style="top:184px">Phone :</div>
    <div class="field right" style="top:184px">Date :</div>
    <div class="field left" style="top:202px">Re :</div>
    <div class="field right" style="top:202px">CC :</div>
    <div class="checks">
      <label><i></i>Urgent</label>
      <label><i></i>For Review</label>
      <label><i></i>Please Comment</label>
      <label><i></i>Please Reply</label>
      <label><i></i>Please Recycle</label>
    </div>
    <div class="watermark" role="img" aria-label="Faint brand watermark"></div>
    <div class="footer-rule"></div>
    <div class="footer-band">
      <span>✆ 555-014-2290</span><span>✆ 555-014-2256</span><span>✉ hello@bellwetherinspect.com</span><span>www.bellwetherinspect.com</span>
    </div>
  </section>

  <!-- Envelope backs -->
  <svg class="envelope-back" style="left:802px;top:83px" width="378" height="169" viewBox="0 0 378 169" aria-hidden="true">
    <rect width="378" height="169" fill="#fff"/>
    <path d="M0 0 H378 L372 22 Q368 30 356 33 L212 66 Q189 71 166 66 L22 33 Q10 30 6 22 Z" fill="#0a4fb0"/>
  </svg>
  <svg class="envelope-back" style="left:789px;top:157px" width="379" height="168" viewBox="0 0 379 168" aria-hidden="true">
    <defs><linearGradient id="envShade" x1="0" y1="0" x2="1" y2="1"><stop offset="0" stop-color="#f6f7f8"/><stop offset="1" stop-color="#e4e7ea"/></linearGradient></defs>
    <rect width="379" height="168" fill="url(#envShade)"/>
    <path d="M0 0 H379 L373 22 Q369 30 357 33 L212 66 Q189 71 167 66 L22 33 Q10 30 6 22 Z" fill="var(--flap-grey)"/>
  </svg>

  <!-- Envelope front -->
  <section class="sheet envelope-front">
    <div class="watermark" role="img" aria-label="Faint brand watermark"></div>
    <div class="brand"><i class="brand-mark"></i>Bellwether<br>Home Inspections</div>
    <div class="footer-rule"></div>
    <div class="footer-band"><span>Street Name, City Name State Zipcode</span><span>www.bellwetherinspect.com</span></div>
  </section>

  <!-- Business card front -->
  <section class="sheet card-front">
    <div class="brand"><i class="brand-mark"></i>Bellwether<br>Home Inspections</div>
    <div class="person">
      <strong>Your Name</strong>
      <em>Title</em>
      <p>✆ 555-014-2290</p>
      <p>✆ 555-014-2256</p>
      <p>✉ hello@bellwetherinspect.com</p>
      <p>◉ www.bellwetherinspect.com</p>
    </div>
    <div class="footer-band">Street Name, City Name State Zipcode</div>
  </section>

  <!-- Business card back -->
  <section class="sheet card-back">
    <div class="watermark" role="img" aria-label="Faint brand watermark"></div>
    <h2>Bellwether<br>Home Inspections</h2>
    <p>www.bellwetherinspect.com</p>
  </section>

  <div class="option-label" style="left:182px">Option-1</div>
  <div class="option-label" style="left:589px">Option-2</div>

</body>
</html>
```